Partial Vehicle Wrap for Vacation Rental Company

We are purchasing new 2024 Valtor Stride Hauler vans for our maintenance team and will be wrapping the vehicles. The wrap will be a partial wrap, meaning it will only cover 50% of the vehicle, the rest will be white. Our company does property management for vacation rentals in Columbia and Lake Murray SC. We have a more modern and clean aesthetic - our website is pinecovecottagesuites.com. I have uploaded our logo as an example of our colors and brand guidelines.

Target Market(s)

Lake Vacation and Family Oriented

Industry/Entity Type

Vacation rental management

Font styles to use
Sans Serif

Colors
0054AA
0677BA
7BADD7
CADEEF
E8F1F8

Requirements
Must have
• Our company name, phone number, brand colors
Nice to have
• Clean lines, modern, easy to read
Should not have
• We don't want this to be too busy, with too much going on.

```html
<!DOCTYPE html>
<html lang="en">
<head>
<meta charset="utf-8">
<title>Pinecove Cottage Suites – Van Wrap Artwork</title>
<link href="https://fonts.googleapis.com/css2?family=Montserrat:wght@700&family=Open+Sans:wght@400;700&display=swap" rel="stylesheet">
<style>
  :root {
    --brand-blue: #1f6db5;
    --ink: #111111;
    --wrap-white: #ffffff;
    --canvas: #eef1f4;
    --panel-edge: #d5dbe2;
    --keys-light: #e6e6e4;
    --keys-dark: #b9b8b3;
  }
  * { box-sizing: border-box; margin: 0; padding: 0; }
  html, body { width: 1200px; height: 1100px; overflow: hidden; }
  body { background: var(--canvas); position: relative; font-family: "Open Sans", Arial, sans-serif; color: var(--ink); }

  .wrap-panel {
    position: absolute;
    background: var(--wrap-white);
    border: 1px solid var(--panel-edge);
    border-radius: 18px;
    overflow: hidden;
  }
  .panel-side-curb { left: 40px; top: 30px; width: 1120px; height: 470px; }
  .panel-side-street { left: 40px; top: 530px; width: 700px; height: 540px; }
  .panel-rear { left: 770px; top: 530px; width: 390px; height: 540px; }

  .swoosh { position: absolute; inset: 0; width: 100%; height: 100%; }
  .swoosh .blue { fill: var(--brand-blue); }
  .swoosh .dark { fill: var(--ink); }

  .brand-name {
    position: absolute;
    font-family: "Montserrat", Arial, sans-serif;
    font-weight: 700;
    color: var(--ink);
    text-transform: uppercase;
    line-height: 1.1;
    text-align: center;
  }
  .brand-name .line { display: block; white-space: nowrap; }

  .keys-art {
    position: absolute;
    border-radius: 14px;
    background: radial-gradient(circle at 45% 40%, var(--keys-light), var(--keys-dark));
  }

  .phone {
    position: absolute;
    display: flex;
    align-items: center;
    gap: 8px;
    font-weight: 700;
    color: var(--ink);
    white-space: nowrap;
    line-height: 1;
  }
  .phone svg { flex: none; }
  .phone-icon circle { fill: none; stroke: var(--brand-blue); stroke-width: 2.5; }
  .phone-icon path { fill: var(--brand-blue); }

  .web {
    position: absolute;
    white-space: nowrap;
    color: var(--ink);
    line-height: 1.2;
  }
  .web .host { font-weight: 700; }
  .web .domain { font-weight: 400; color: var(--brand-blue); }
</style>
</head>
<body>

<section class="wrap-panel panel-side-curb" aria-label="Curb side wrap">
  <svg class="swoosh" viewBox="0 0 1120 470" preserveAspectRatio="none" aria-hidden="true">
    <path class="dark" d="M0 180 Q140 290 400 318 Q150 300 0 160 Z"/>
    <path class="blue" d="M0 205 Q150 305 400 324 Q140 290 0 230 Z"/>
    <path class="blue" d="M720 214 Q1000 200 1100 330 L1086 338 Q980 220 720 214 Z"/>
    <path class="dark" d="M1086 338 Q990 232 800 214 Q1000 214 1100 330 Z"/>
  </svg>

  <h1 class="brand-name" style="left:300px; top:55px; width:600px;">
    <span class="line" style="font-size:54px; letter-spacing:9px;">Pinecove</span>
    <span class="line" style="font-size:34px; letter-spacing:6px;">Cottage Suites</span>
  </h1>

  <div class="keys-art" role="img" aria-label="Silver house keys on a ring with a house-shaped key tag" style="left:420px; top:185px; width:200px; height:180px;"></div>

  <div class="phone" style="left:640px; top:295px; font-size:36px;">
    <svg class="phone-icon" width="36" height="36" viewBox="0 0 36 36" aria-hidden="true"><circle cx="18" cy="18" r="15"/><path d="M12 10c1-1 2-1 3 0l2 3c.5 1 0 2-1 2.5 1 2.5 2.5 4 5 5 .5-1 1.5-1.5 2.5-1l3 2c1 1 1 2 0 3-2 2-5 2-9-1s-6-7-6-10c0-1.5 0-2.5.5-3.5z"/></svg>
    <span>803 555 0142</span>
  </div>
  <p class="web" style="left:500px; top:385px; font-size:25px;"><span class="host">www.pinecove</span><span class="domain">cottagesuites.com</span></p>
</section>

<section class="wrap-panel panel-side-street" aria-label="Street side wrap">
  <svg class="swoosh" viewBox="0 0 700 540" preserveAspectRatio="none" aria-hidden="true">
    <path class="blue" d="M0 380 Q90 300 260 290 Q100 320 10 410 Z"/>
    <path class="dark" d="M10 410 Q100 330 240 296 Q110 340 18 420 Z"/>
    <path class="blue" d="M540 345 Q650 330 700 200 L700 240 Q650 345 540 345 Z"/>
    <path class="dark" d="M570 346 Q660 335 700 240 L700 256 Q655 352 570 346 Z"/>
  </svg>

  <h2 class="brand-name" style="left:50px; top:80px; width:600px;">
    <span class="line" style="font-size:50px; letter-spacing:8px;">Pinecove</span>
    <span class="line" style="font-size:31px; letter-spacing:6px;">Cottage Suites</span>
  </h2>

  <div class="keys-art" role="img" aria-label="Silver house keys on a ring with a house-shaped key tag" style="left:300px; top:200px; width:220px; height:190px;"></div>

  <div class="phone" style="left:90px; top:410px; font-size:34px;">
    <svg class="phone-icon" width="34" height="34" viewBox="0 0 36 36" aria-hidden="true"><circle cx="18" cy="18" r="15"/><path d="M12 10c1-1 2-1 3 0l2 3c.5 1 0 2-1 2.5 1 2.5 2.5 4 5 5 .5-1 1.5-1.5 2.5-1l3 2c1 1 1 2 0 3-2 2-5 2-9-1s-6-7-6-10c0-1.5 0-2.5.5-3.5z"/></svg>
    <span>803 555 0142</span>
  </div>
  <p class="web" style="left:40px; top:465px; font-size:24px;"><span class="host">www.pinecove</span><span class="domain">cottagesuites.com</span></p>
</section>

<section class="wrap-panel panel-rear" aria-label="Rear doors wrap">
  <svg class="swoosh" viewBox="0 0 390 540" preserveAspectRatio="none" aria-hidden="true">
    <path class="blue" d="M0 150 Q50 30 210 25 Q70 50 10 175 Z"/>
    <path class="dark" d="M0 175 Q45 55 170 32 Q60 72 0 198 Z"/>
    <path class="blue" d="M275 300 Q360 292 390 205 L390 240 Q355 300 275 300 Z"/>
    <path class="dark" d="M300 302 Q365 298 390 240 L390 256 Q358 308 300 302 Z"/>
  </svg>

  <h2 class="brand-name" style="left:85px; top:92px; width:290px;">
    <span class="line" style="font-size:32px; letter-spacing:4px;">Pinecove</span>
    <span class="line" style="font-size:20px; letter-spacing:3px;">Cottage Suites</span>
  </h2>

  <div class="keys-art" role="img" aria-label="Silver house keys on a ring with a house-shaped key tag" style="left:60px; top:200px; width:200px; height:190px;"></div>

  <div class="phone" style="left:150px; top:420px; font-size:30px;">
    <svg class="phone-icon" width="30" height="30" viewBox="0 0 36 36" aria-hidden="true"><circle cx="18" cy="18" r="15"/><path d="M12 10c1-1 2-1 3 0l2 3c.5 1 0 2-1 2.5 1 2.5 2.5 4 5 5 .5-1 1.5-1.5 2.5-1l3 2c1 1 1 2 0 3-2 2-5 2-9-1s-6-7-6-10c0-1.5 0-2.5.5-3.5z"/></svg>
    <span>803 555 0142</span>
  </div>
  <p class="web" style="left:22px; top:478px; font-size:19px;"><span class="host">www.pinecove</span><span class="domain">cottagesuites.com</span></p>
</section>

</body>
</html>
```